Business card design needed

We do excavation, cartage and contracting
I would quote like to have a picture of my digger as the whole back ground and the words on top. If that looks any good
Otherwise please feel free to come up with any other cool options

Cheers Marc

KLR Contracting
Excavation, Cartage, Contracting
Marcus Prewitt
www.klr-example.co.nz
021 584 067
marc@klr-example.co.nz

```html
<!DOCTYPE html>
<html lang="en">
<head>
<meta charset="utf-8">
<title>KLR Contracting – Business Card</title>
<link href="https://fonts.googleapis.com/css2?family=Ubuntu:wght@400;500;700&display=swap" rel="stylesheet">
<style>
  :root {
    --page-bg: #e8e5e0;
    --forest: #1f5a2b;
    --forest-light: #2f7a3c;
    --ink-green: #1b4a23;
    --mark-tint: #e3ece3;
    --paper: #ffffff;
    --photo-sky: #8fb0c8;
    --photo-trees: #4d7a35;
    --photo-dirt: #8b6a49;
    --photo-dirt-dark: #6e5238;
  }
  * { margin: 0; padding: 0; box-sizing: border-box; }
  html, body {
    width: 1200px; height: 900px; overflow: hidden;
    background: var(--page-bg);
    font-family: "Ubuntu", sans-serif;
  }
  .card {
    position: absolute; left: 250px;
    width: 700px; height: 400px;
    overflow: hidden;
    box-shadow: 0 6px 18px rgba(0,0,0,0.18);
  }
  .card-back { top: 33px; }
  .card-front { top: 467px; background: var(--paper); }

  .digger-photo {
    position: absolute; inset: 0;
    background:
      linear-gradient(160deg, var(--photo-sky) 0%, var(--photo-trees) 22%, var(--photo-trees) 42%, var(--photo-dirt) 62%, var(--photo-dirt-dark) 100%);
  }
  .back-name {
    position: absolute; left: 420px; top: 150px;
    font-weight: 700; font-size: 84px; letter-spacing: 2px;
    color: var(--forest);
  }

  .front-shape { position: absolute; inset: 0; }
  .services {
    position: absolute; left: 28px; top: 24px;
    color: var(--paper); font-size: 26px; line-height: 1.12;
  }
  .contact-web {
    position: absolute; left: 24px; bottom: 28px;
    color: var(--paper); font-size: 21px; line-height: 1.3;
    white-space: nowrap;
  }
  .brand-name {
    position: absolute; right: 40px; top: 26px;
    font-weight: 700; font-size: 64px; letter-spacing: 2px;
    color: var(--forest);
  }
  .person-name {
    position: absolute; left: 350px; top: 172px;
    font-weight: 700; font-size: 40px;
    color: var(--ink-green);
    white-space: nowrap;
  }
  .phone {
    position: absolute; right: 36px; bottom: 30px;
    font-weight: 500; font-size: 34px;
    color: var(--ink-green);
    white-space: nowrap;
  }
</style>
</head>
<body>

<section class="card card-back">
  <div class="digger-photo" role="img" aria-label="Photograph of a yellow digger working on a dirt bank above green bush"></div>
  <div class="back-name">KLR</div>
</section>

<section class="card card-front">
  <svg class="front-shape" width="700" height="400" viewBox="0 0 700 400" aria-hidden="true">
    <defs>
      <linearGradient id="forestFill" x1="0" y1="0" x2="1" y2="1">
        <stop offset="0" stop-color="var(--forest-light)"/>
        <stop offset="1" stop-color="var(--forest)"/>
      </linearGradient>
    </defs>
    <path d="M0 0 H410 C300 90 290 280 335 400 H0 Z" fill="url(#forestFill)"/>
    <text x="140" y="290" font-family="Ubuntu, sans-serif" font-weight="700" font-size="210"
          fill="var(--mark-tint)" opacity="0.25">KLR</text>
  </svg>

  <div class="services">Contracting Excavation<br>Cartage<br>Contracting</div>
  <div class="contact-web">marc@klr-example.co.nz<br>www.klr-example.co.nz</div>

  <div class="brand-name">KLR</div>
  <div class="person-name">Marcus Prewitt</div>
  <div class="phone">Ph.021 584 067</div>
</section>

</body>
</html>
```